Borrowdale Equity Business Card

Looking for a design for our business cards. Need to look corporate and outstanding. I have enclosed our logos for the company. Borrowdale equity is an investment firm for high level clients looking for advisory in their investments. White background or black is good. We will like to double sided options maybe at the back with just the logo of the firm.

Example of the info for the business card:

Marcus Heller
Managing Director

Panama Phone +507 391 4786
Switzerland Phone +41 43 917 2648
test@borrowdale-equity-example.com
www.borrowdale-equity-example.com

Industry/Entity Type

Investment

```html
<!DOCTYPE html>
<html lang="en">
<head>
<meta charset="utf-8">
<title>Borrowdale Equity – Business Card</title>
<link rel="stylesheet" href="https://fonts.googleapis.com/css2?family=Federo&family=Sorts+Mill+Goudy&family=Cinzel:wght@400&display=swap">
<style>
  :root {
    --ink-black: #000000;
    --paper-grey: #ececec;
    --paper-light: #e9e9e9;
    --paper-white: #ffffff;
    --gold: #a8821f;
    --gold-band: #b0871e;
    --navy: #13236b;
    --navy-logo: #1a2f74;
    --faint-logo: #d8dce4;
    --faint-accent: #e3e0d8;
  }
  * { margin: 0; padding: 0; box-sizing: border-box; }
  html, body { width: 835px; height: 1200px; overflow: hidden; background: var(--paper-white); }
  .sheet { position: relative; width: 835px; height: 1200px; }
  .band { position: absolute; left: 0; width: 835px; }
  .band--header { top: 0; height: 122px; background: var(--ink-black); }
  .band--front { top: 122px; height: 359px; background: var(--paper-grey); }
  .band--footer { top: 481px; height: 60px; background: var(--ink-black); }
  .band--gap { top: 541px; height: 119px; background: var(--paper-white); }
  .band--back-top { top: 660px; height: 108px; background: var(--paper-light); }
  .band--rule { top: 768px; height: 12px; background: var(--gold-band); }
  .band--back { top: 780px; height: 364px; background: var(--ink-black); }
  .band--back-bottom { top: 1144px; height: 56px; background: var(--paper-light); }

  .holder-name {
    position: absolute; left: 29px; top: 30px;
    font-family: "Federo", sans-serif; font-size: 33px; color: var(--gold);
    letter-spacing: 0.5px;
  }
  .holder-role {
    position: absolute; left: 32px; top: 74px;
    font-family: "Sorts Mill Goudy", serif; font-size: 22px; color: var(--gold);
  }

  .wordmark {
    position: absolute; display: flex; align-items: center; gap: 22px;
    font-family: "Cinzel", serif; font-weight: 400; white-space: nowrap;
  }
  .wordmark__square { display: block; flex: none; }
  .wordmark--faint { left: 78px; top: 222px; font-size: 58px; color: var(--faint-logo); }
  .wordmark--faint .wordmark__square { width: 60px; height: 60px; background: var(--faint-accent); }
  .wordmark--back { left: 100px; top: 895px; font-size: 56px; color: var(--navy-logo); }
  .wordmark--back .wordmark__square { width: 56px; height: 56px; background: var(--gold); }

  .contact {
    position: absolute; right: 9px; top: 366px; text-align: right;
    font-family: "Federo", sans-serif; font-variant: small-caps;
    color: var(--navy); font-size: 22px; line-height: 27.5px; letter-spacing: 1px;
  }
  .contact__line--web { font-variant: normal; text-transform: uppercase; font-size: 17px; }
</style>
</head>
<body>
<div class="sheet">
  <div class="band band--header"></div>
  <div class="band band--front"></div>
  <div class="band band--footer"></div>
  <div class="band band--gap"></div>
  <div class="band band--back-top"></div>
  <div class="band band--rule"></div>
  <div class="band band--back"></div>
  <div class="band band--back-bottom"></div>

  <div class="holder-name">Marcus Heller</div>
  <div class="holder-role">Managing Director</div>

  <div class="wordmark wordmark--faint" aria-hidden="true">
    <span class="wordmark__square"></span>Borrowdale Equity
  </div>

  <div class="contact">
    <p class="contact__line">Panama Phone +507 391 4786</p>
    <p class="contact__line">Switzerland Phone +41 43 917 2648</p>
    <p class="contact__line contact__line--web">test@borrowdale-equity-example.com</p>
    <p class="contact__line contact__line--web">www.borrowdale-equity-example.com</p>
  </div>

  <div class="wordmark wordmark--back">
    <span class="wordmark__square"></span>Borrowdale Equity
  </div>
</div>
</body>
</html>
```